Webdesign für Fahrschule
Petra Lindqvor
Sehr ansprechendes, modernes und übersichtliches Design, welches das Unternehmen sehr gut widerspiegelt
Zielgruppe
Fahrschule mit fach- und sachgerechter Fahrschulausbildung in allen Zweiradklassen und im PKW-Bereich sowie Ausbildung auf Automatikfahrzeugen und Führerscheinausbildung für Behinderte
Aufgabenstellung
Keine Kopie der alten Seite
Nutzerfreundliche Unternehmenswebseite
Design soll frisch, modern und aussagekräftig erscheinen

```html
<!DOCTYPE html>
<html lang="de">
<head>
<meta charset="utf-8">
<title>Fahrschule Petra Lindqvor – Webdesign</title>
<link href="https://fonts.googleapis.com/css2?family=Open+Sans:wght@400;600;700&family=Ubuntu:wght@400;500;700&display=swap" rel="stylesheet">
<style>
:root{
  --red:#e3261b;
  --ink:#1a1a1a;
  --text:#555;
  --muted:#8a8a8a;
  --soft:#f4f4f4;
  --line:#e4e4e4;
  --black:#111;
  --white:#fff;
  --hero:linear-gradient(180deg,#2e221c 0%,#6b3c22 22%,#c4692c 45%,#eaa053 58%,#b35d26 75%,#3c2418 100%);
  --photo-girl:radial-gradient(ellipse at 62% 38%,#e9c6a6 0%,#d7a98a 18%,transparent 40%),linear-gradient(135deg,#9fb6cf 0%,#c9a58a 40%,#7d93ad 62%,#2f5f9c 100%);
  --photo-car:radial-gradient(ellipse at 30% 40%,#c39a78 0%,transparent 35%),radial-gradient(ellipse at 70% 45%,#b58d6c 0%,transparent 35%),linear-gradient(135deg,#4a3e34,#8a6a50 50%,#2f2925);
}
*{box-sizing:border-box;margin:0;padding:0}
html,body{width:1200px;height:3550px;overflow:hidden}
body{position:relative;background:var(--white);font-family:"Open Sans",Arial,sans-serif;color:var(--text)}
.abs{position:absolute}
h1,h2,h3,h4{font-family:"Ubuntu","Open Sans",sans-serif;color:var(--ink)}
.red{color:var(--red)}
.btn{display:inline-block;background:var(--black);color:var(--white);border-radius:4px;font-family:"Open Sans",sans-serif;text-align:center}

/* Intro */
.intro{left:0;top:0;width:1200px;height:830px;background:linear-gradient(160deg,#fafafa 0%,#ececec 60%,#f7f7f7 100%)}
.intro-title{position:absolute;left:0;top:46px;width:1200px;text-align:center;font-family:"Open Sans",sans-serif;font-weight:600;font-size:56px;line-height:64px;color:var(--muted)}
.intro-band{left:0;top:830px;width:1200px;height:15px;background:var(--black)}
.preview{left:210px;top:262px;width:780px;height:495px;background:var(--white);box-shadow:0 10px 40px rgba(0,0,0,.18);overflow:hidden}
.preview-mobile{left:140px;top:318px;width:232px;height:505px;background:var(--white);box-shadow:0 12px 40px rgba(0,0,0,.25);overflow:hidden;border-radius:6px}
.preview-mobile p{font-size:9.5px;line-height:19px;color:#666}

/* Section headings */
.view-label{font-family:"Open Sans",sans-serif;font-size:31px;color:var(--ink);font-weight:400}

/* Shared site pieces */
.topbar{position:absolute;left:0;top:0;width:100%;background:var(--black);color:var(--white);text-align:center}
.hero{position:absolute;left:0;width:100%;background:var(--hero)}
.site-head{position:absolute;left:0;width:100%;background:rgba(255,255,255,.55)}
.brand small{display:block;font-size:7px;color:var(--ink)}
.brand b{font-weight:600;color:var(--ink)}
.nav span{margin-left:14px}
.nav .on{border-bottom:1px solid var(--red)}
.hero-card{position:absolute;background:var(--white);padding:20px 20px}
.hero-card h1{font-weight:700;text-transform:uppercase}
.features{position:absolute;left:0;width:100%;background:var(--soft)}
.feature{position:absolute;text-align:center}
.feature h4{font-weight:500;text-transform:uppercase;letter-spacing:.3px}
.feature p{color:#444}
.photo{background:var(--photo-girl)}
.check{display:inline-block;vertical-align:top}
.card{position:absolute;border:1px solid var(--line);background:var(--white)}
.car{background:linear-gradient(180deg,#4f7ec0,#1d3f78);border-radius:6px 10px 3px 3px}
.deco{background:#efefef;transform:skewX(-30deg)}

/* Desktop view */
.desk{left:28px;top:946px;width:766px;height:2320px}
.desk .topbar{height:21px;font-size:7px;line-height:21px}
.desk .hero{top:21px;height:326px}
.desk .features{top:347px;height:92px}
.desk .feature{width:140px;top:12px}
.desk .feature h4{font-size:9.5px;margin-top:6px}
.desk .feature p{font-size:6px;line-height:9px;margin-top:4px}
.desk-text{font-size:6px;line-height:10px;color:#777}
.desk-item{display:flex;gap:10px;margin-top:12px}
.desk-item b{display:block;font-size:6.5px;color:var(--ink);margin-bottom:2px}
.k-card{width:195px;height:91px;padding:12px 10px}
.k-card .car{width:40px;height:18px;display:inline-block;vertical-align:middle}
.k-card h4{display:inline-block;font-size:7px;font-weight:700;margin-left:14px;vertical-align:middle;text-transform:uppercase}
.k-card p{font-size:5.8px;line-height:10px;color:#888;margin-top:8px}

/* Mobile view */
.mob{left:871px;top:946px;width:244px;height:2480px}
.mob .topbar{height:42px;font-size:9px;line-height:14px;padding-top:7px}
.mob .hero{top:42px;height:220px}
.mob p{font-size:9.5px;line-height:20px;color:#555}
.mob .features{top:449px;height:369px}
.mob .feature{left:0;width:244px}
.mob .feature h4{font-size:12.5px;margin-top:12px}
.mob .feature p{font-size:8.5px;line-height:12px;margin-top:6px;padding:0 40px}
.m-card{left:8px;width:228px;height:200px;padding:18px 14px}
.m-card .car{width:54px;height:24px}
.m-card h4{font-size:11.5px;font-weight:500;margin-top:18px;text-transform:uppercase}
.m-card p{font-size:9.5px;line-height:20px;color:#888;margin-top:8px}

.footer-col h5{font-family:"Open Sans",sans-serif;font-size:7px;color:var(--red);font-weight:700;margin-bottom:6px}
.footer-col p{font-size:6px;line-height:9px;color:#444}
</style>
</head>
<body>

<!-- Intro header with flat desktop and mobile previews -->
<section class="abs intro">
  <h2 class="intro-title">Fahrschule<br>Petra Lindqvor</h2>
  <div class="abs preview">
    <div class="topbar" style="height:20px;font-size:7px;line-height:20px">Schnell, einfach, erfolgreich – jetzt Führerschein machen!</div>
    <div class="hero" style="top:20px;height:330px" role="img" aria-label="Foto: schwarzes Auto fährt mit Bewegungsunschärfe im Abendlicht"></div>
    <div class="site-head" style="top:26px;height:40px"></div>
    <div class="abs brand" style="left:80px;top:36px;font-size:9px;line-height:11px"><small>Fahrschule</small><b>Petra Lindqvor</b></div>
    <div class="abs nav" style="right:90px;top:44px;font-size:7px;color:#222"><span class="on">Start</span><span>Anmeldung</span><span>Aufbauseminar</span><span>Kontakt</span></div>
    <div class="hero-card" style="left:430px;top:110px;width:270px;height:155px">
      <h1 style="font-size:19px;line-height:25px">Dein Führerschein<br>in <span class="red">Chemnitz</span></h1>
      <p style="font-size:6.5px;line-height:12px;margin-top:10px">Wir bringen Sie sicher auf die Straße! Als erfahrene Fahrschule bieten wir Ihnen fach- und sachgerechte Fahrausbildung in allen Zweiradklassen und im PKW-Bereich.</p>
      <span class="btn" style="font-size:6.5px;padding:4px 10px;margin-top:10px">Jetzt anmelden ➚</span>
    </div>
    <div class="features" style="top:350px;height:145px">
      <div class="feature" style="left:170px;top:24px;width:160px"><svg width="14" height="14"><rect x="2" y="2" width="10" height="10" rx="2" fill="#d4a21c"/></svg><h4 style="font-size:10px;margin-top:6px;text-transform:none">Erfahrene Fahrlehrer</h4><p style="font-size:6.5px;line-height:9px">Professionelle Anleitung für deinen sicheren Start.</p></div>
      <div class="feature" style="left:330px;top:24px;width:160px"><svg width="14" height="14"><rect x="1" y="5" width="12" height="6" rx="2" fill="#c0392b"/></svg><h4 style="font-size:10px;margin-top:6px">Moderne Fahrzeuge</h4><p style="font-size:6.5px;line-height:9px">Lerne mit topaktuellen, sicheren Fahrzeugen.</p></div>
      <div class="feature" style="left:490px;top:24px;width:160px"><svg width="14" height="14"><circle cx="7" cy="7" r="5.5" fill="none" stroke="#e3261b" stroke-width="1.5"/><path d="M7 4v3.5l2 1" stroke="#e3261b" fill="none"/></svg><h4 style="font-size:10px;margin-top:6px">Flexible Kurszeiten</h4><p style="font-size:6.5px;line-height:9px">Professionelle Anleitung für deinen sicheren Start.</p></div>
    </div>
  </div>

  <div class="abs preview-mobile">
    <div class="abs photo" style="left:0;top:0;width:232px;height:204px" role="img" aria-label="Foto: junge Fahrschülerin am Autofenster zeigt Daumen hoch"></div>
    <div class="abs" style="left:14px;top:237px;width:210px">
      <h3 style="font-size:11px;font-weight:700;text-transform:uppercase">Hier bist du genau <span class="red">richtig</span>!</h3>
      <svg style="margin-top:18px;display:block" width="17" height="17"><circle cx="8.5" cy="8.5" r="8.5" fill="#e3261b"/><path d="M5 8.8l2.5 2.5 4.5-5" stroke="#fff" stroke-width="1.7" fill="none"/></svg>
      <h4 style="font-size:9.5px;font-weight:700;margin-top:6px;font-family:'Open Sans',sans-serif">Begleitung mit Lern-App</h4>
      <p>Wir begleiten Deinen Lernfortschritt mit einer Lern-App für unterwegs.<br>So bist Du auf Deine Theorieprüfung optimal vorbereitet.</p>
      <svg style="margin-top:18px;display:block" width="17" height="17"><circle cx="8.5" cy="8.5" r="8.5" fill="#e3261b"/><path d="M5 8.8l2.5 2.5 4.5-5" stroke="#fff" stroke-width="1.7" fill="none"/></svg>
      <h4 style="font-size:9.5px;font-weight:700;margin-top:6px;font-family:'Open Sans',sans-serif">Keine lästigen Behördengänge</h4>
      <p>Deine Anmelde- und Prüfungsunterlagen musst Du nicht selbst zu den Ämtern tragen. Wir übernehmen Deine Behördengänge und</p>
    </div>
  </div>
</section>
<div class="abs intro-band"></div>

<h2 class="abs view-label" style="left:26px;top:888px">Desktop Ansicht</h2>
<h2 class="abs view-label" style="left:871px;top:888px">Mobile Ansicht</h2>

<!-- ============ Desktop view ============ -->
<main class="abs desk">
  <div class="topbar">Schnell, einfach, erfolgreich – jetzt Führerschein machen!</div>
  <div class="hero" role="img" aria-label="Foto: schwarzes Auto fährt mit Bewegungsunschärfe im Abendlicht"></div>
  <div class="site-head" style="top:28px;height:40px"></div>
  <div class="abs brand" style="left:80px;top:44px;font-size:9px;line-height:11px"><small>Fahrschule</small><b>Petra Lindqvor</b></div>
  <div class="abs nav" style="right:84px;top:50px;font-size:7px;color:#222"><span class="on">Start</span><span>Anmeldung</span><span>Aufbauseminar</span><span>Kontakt</span></div>
  <div class="hero-card" style="left:424px;top:134px;width:267px;height:156px">
    <h1 style="font-size:19px;line-height:25px">Dein Führerschein<br>in <span class="red">Chemnitz</span></h1>
    <p style="font-size:6.5px;line-height:12px;margin-top:10px">Wir bringen Sie sicher auf die Straße! Als erfahrene Fahrschule bieten wir Ihnen fach- und sachgerechte Fahrausbildung in allen Zweiradklassen und im PKW-Bereich.</p>
    <span class="btn" style="font-size:6.5px;padding:4px 10px;margin-top:10px">Jetzt anmelden ➚</span>
  </div>

  <div class="features">
    <div class="feature" style="left:143px"><svg width="14" height="14"><rect x="2" y="2" width="10" height="10" rx="2" fill="#d4a21c"/></svg><h4 style="text-transform:none">Erfahrene Fahrlehrer</h4><p>Professionelle Anleitung für deinen sicheren Start.</p></div>
    <div class="feature" style="left:329px"><svg width="14" height="14"><rect x="1" y="5" width="12" height="6" rx="2" fill="#c0392b"/></svg><h4>Moderne Fahrzeuge</h4><p>Lerne mit topaktuellen, sicheren Fahrzeugen.</p></div>
    <div class="feature" style="left:508px"><svg width="14" height="14"><circle cx="7" cy="7" r="5.5" fill="none" stroke="#e3261b" stroke-width="1.5"/><path d="M7 4v3.5l2 1" stroke="#e3261b" fill="none"/></svg><h4>Flexible Kurszeiten</h4><p>Professionelle Anleitung für deinen sicheren Start.</p></div>
  </div>

  <!-- Hier bist du genau richtig -->
  <section class="abs" style="left:97px;top:510px;width:245px">
    <h3 style="font-size:11.5px;font-weight:700;text-transform:uppercase">Hier bist du genau <span class="red">richtig</span>!</h3>
    <p class="desk-text" style="margin-top:4px">Mobil sein, frei sein, dein Führerschein. Warum wir?</p>
    <div class="desk-item"><svg class="check" width="17" height="17"><circle cx="8.5" cy="8.5" r="8.5" fill="#e3261b"/><path d="M5 8.8l2.5 2.5 4.5-5" stroke="#fff" stroke-width="1.6" fill="none"/></svg><div class="desk-text"><b>Begleitung mit Lern-App</b>Wir begleiten Deinen Lernfortschritt mit einer Lern-App für unterwegs. So bist Du auf Deine Theorieprüfung optimal vorbereitet.</div></div>
    <div class="desk-item"><svg class="check" width="17" height="17"><circle cx="8.5" cy="8.5" r="8.5" fill="#e3261b"/><path d="M5 8.8l2.5 2.5 4.5-5" stroke="#fff" stroke-width="1.6" fill="none"/></svg><div class="desk-text"><b>Keine lästigen Behördengänge</b>Deine Anmelde- und Prüfungsunterlagen musst Du nicht selbst zu den Ämtern tragen. Wir übernehmen Deine Behördengänge und kümmern uns um eine reibungslose Abwicklung.</div></div>
    <div class="desk-item"><svg class="check" width="17" height="17"><circle cx="8.5" cy="8.5" r="8.5" fill="#e3261b"/><path d="M5 8.8l2.5 2.5 4.5-5" stroke="#fff" stroke-width="1.6" fill="none"/></svg><div class="desk-text"><b>Einzigartige Lernatmosphäre</b>In lockerer Atmosphäre wirst Du alles lernen, was Du zum Bestehen Deiner theoretischen und praktischen Prüfung brauchst. Erlebe eine herzliche, humorvolle und kompetente Ausbildung und kröne das Ganze mit Deinem Führerschein.</div></div>
    <span class="btn" style="font-size:6px;padding:4px 10px;margin:14px 0 0 27px">Jetzt anmelden ➚</span>
  </section>
  <div class="abs photo" style="left:374px;top:504px;width:320px;height:273px" role="img" aria-label="Foto: junge Fahrschülerin am Autofenster zeigt Daumen hoch"></div>

  <!-- Führerscheinklassen -->
  <div class="abs deco" style="left:90px;top:832px;width:120px;height:124px"></div>
  <h2 class="abs" style="left:181px;top:864px;width:400px;text-align:center;font-size:12px;line-height:18px;font-weight:700;text-transform:uppercase">Folgende <span class="red">Führerscheinklassen</span><br>kannst du bei uns machen.</h2>

  <div class="card k-card" style="left:82px;top:924px"><span class="car"></span><h4>BF 17 | PKW ab 17 Jahren</h4><p>Lorem ipsum dolor sit amet, consetetur sadipscing elitr, sed diam nonumy eirmod tempor invidunt ut labore et dolore magna aliquyam erat, sed diam voluptua. At vero</p></div>
  <div class="card k-card" style="left:285px;top:924px"><span class="car"></span><h4>BF 17 | PKW ab 17 Jahren</h4><p>Lorem ipsum dolor sit amet, consetetur sadipscing elitr, sed diam nonumy eirmod tempor invidunt ut labore et dolore magna aliquyam erat, sed diam voluptua. At vero</p></div>
  <div class="card k-card" style="left:487px;top:924px"><span class="car"></span><h4>BE | PKW mit Anhänger</h4><p>Lorem ipsum dolor sit amet, consetetur sadipscing elitr, sed diam nonumy eirmod tempor invidunt ut labore et dolore magna aliquyam erat, sed diam voluptua. At vero</p></div>
  <div class="card k-card" style="left:82px;top:1025px"><span class="car"></span><h4>Klasse B96</h4><p>Lorem ipsum dolor sit amet, consetetur sadipscing elitr, sed diam nonumy eirmod tempor invidunt ut labore et dolore magna aliquyam erat, sed diam voluptua. At vero</p></div>
  <div class="card k-card" style="left:285px;top:1025px"><span class="car"></span><h4>Klasse A</h4><p>Lorem ipsum dolor sit amet, consetetur sadipscing elitr, sed diam nonumy eirmod tempor invidunt ut labore et dolore magna aliquyam erat, sed diam voluptua. At vero</p></div>
  <div class="card k-card" style="left:487px;top:1025px"><span class="car"></span><h4>Klasse A2</h4><p>Lorem ipsum dolor sit amet, consetetur sadipscing elitr, sed diam nonumy eirmod tempor invidunt ut labore et dolore magna aliquyam erat, sed diam voluptua. At vero</p></div>
  <div class="card k-card" style="left:183px;top:1125px"><span class="car"></span><h4 style="text-transform:none">Klasse A1</h4><p>Lorem ipsum dolor sit amet, consetetur sadipscing elitr, sed diam nonumy eirmod tempor invidunt ut labore et dolore magna aliquyam erat, sed diam voluptua. At vero</p></div>
  <div class="card k-card" style="left:387px;top:1125px"><span class="car"></span><h4 style="text-transform:none">Klasse AM</h4><p>Lorem ipsum dolor sit amet, consetetur sadipscing elitr, sed diam nonumy eirmod tempor invidunt ut labore et dolore magna aliquyam erat, sed diam voluptua. At vero</p></div>
  <span class="abs btn" style="left:346px;top:1235px;font-size:6px;padding:3px 9px">Mehr erfahren</span>

  <!-- Bewertungen -->
  <section class="abs" style="left:0;top:1310px;width:766px;height:262px;background:var(--soft)">
    <h2 class="abs" style="left:0;top:50px;width:766px;text-align:center;font-size:11.5px;font-weight:700;text-transform:uppercase">Bewertungen, die für sich sprechen!</h2>
    <p class="abs" style="left:0;top:70px;width:766px;text-align:center;font-size:5.5px">Von Fahranfängern bis Profis – echte Bewertungen, die unsere Qualität beweisen.</p>
    <div class="abs" style="left:217px;top:96px;width:332px;height:123px;background:var(--white);padding:24px 18px">
      <h4 style="font-size:9.5px;font-weight:500">10 JAHRE ERFAHRUNG</h4>
      <p class="desk-text" style="width:190px;margin-top:6px;font-size:5.5px;line-height:9px">Lorem ipsum dolor sit amet, consetetur sadipscing elitr, sed diam nonumy eirmod tempor invidunt ut labore et dolore magna aliquyam erat, sed diam voluptua.</p>
      <span class="btn" style="font-size:6px;padding:3px 10px;margin-top:8px">Jetzt anmelden ➚</span>
      <div class="abs" style="left:219px;top:20px;width:94px;height:68px;background:var(--soft);text-align:center;padding-top:10px">
        <div style="font-size:10px;color:var(--ink)">4,8</div>
        <div style="font-size:8px;color:var(--ink);letter-spacing:1px">★★★★★</div>
        <div style="font-size:5.5px;line-height:8px">Unser Bewertung<br>bei Kundenportal</div>
      </div>
    </div>
  </section>

  <!-- Gute Gründe -->
  <div class="abs" style="left:75px;top:1632px;width:292px;height:250px;background:var(--photo-car)" role="img" aria-label="Foto: junger Fahrschüler am Steuer mit Fahrlehrer auf dem Beifahrersitz"></div>
  <svg class="abs" style="left:235px;top:1740px" width="140" height="145"><polygon points="132,0 132,145 40,145 70,108 110,108" fill="#fff"/><polygon points="0,145 30,108 56,108 26,145" fill="#fff"/></svg>
  <section class="abs" style="left:414px;top:1641px;width:240px">
    <h3 style="font-size:11.5px;line-height:16px;font-weight:700;text-transform:uppercase">Gute Gründe für den<br><span class="red">Führerschein mit 17</span></h3>
    <p class="desk-text" style="margin-top:6px;font-size:5.5px">Bist Du bereit für das Begleitete Fahren ab 17? Na dann los!<br>Es gibt gute Gründe, weshalb sich das BF17 für Dich lohnt:</p>
    <div class="desk-item" style="margin-top:14px"><svg class="check" width="17" height="17"><circle cx="8.5" cy="8.5" r="8.5" fill="#e3261b"/><path d="M5 8.8l2.5 2.5 4.5-5" stroke="#fff" stroke-width="1.6" fill="none"/></svg><div class="desk-text" style="font-size:5.5px"><b>Sicherer Start in die Fahrpraxis</b>Das Autofahren mit einer Begleitperson ist ein entspannter und sicherer Start in die Fahrpraxis.</div></div>
    <div class="desk-item" style="margin-top:14px"><svg class="check" width="17" height="17"><circle cx="8.5" cy="8.5" r="8.5" fill="#e3261b"/><path d="M5 8.8l2.5 2.5 4.5-5" stroke="#fff" stroke-width="1.6" fill="none"/></svg><div class="desk-text" style="font-size:5.5px"><b>Kein Stress im Abi</b>Wenn Du Deine Fahrprüfung kurz vor Deinem 17. Geburtstag ablegst, kollidieren die Prüfungen nicht mit Abi-Lernstress in der Schule.</div></div>
    <div class="desk-item" style="margin-top:14px"><svg class="check" width="17" height="17"><circle cx="8.5" cy="8.5" r="8.5" fill="#e3261b"/><path d="M5 8.8l2.5 2.5 4.5-5" stroke="#fff" stroke-width="1.6" fill="none"/></svg><div class="desk-text" style="font-size:5.5px"><b>Geringere Unfallgefahr</b>Jugendliche, die beim BF17 mitgemacht haben, verursachen später rund 20% weniger Unfälle als diejenigen, die darauf verzichtet haben.</div></div>
    <span class="btn" style="font-size:6px;padding:3px 10px;margin:12px 0 0 27px">Jetzt anmelden ➚</span>
  </section>

  <!-- Karte -->
  <div class="abs" style="left:0;top:1928px;width:766px;height:273px;background:linear-gradient(160deg,#eef0f3,#e6e9ee 50%,#eef1ee)" role="img" aria-label="Karte: Lage der Fahrschule im Ortsteil"></div>
  <svg class="abs" style="left:374px;top:2026px" width="16" height="22"><path d="M8 0a8 8 0 0 1 8 8c0 6-8 14-8 14S0 14 0 8a8 8 0 0 1 8-8z" fill="#e3261b"/><circle cx="8" cy="8" r="3" fill="#fff"/></svg>

  <!-- Footer -->
  <footer class="abs" style="left:0;top:2237px;width:766px">
    <div class="abs brand" style="left:108px;top:0;font-size:8px;line-height:10px"><small>Fahrschule</small><b>Petra Lindqvor</b>
      <p style="font-size:5.5px;line-height:9px;color:#444;margin-top:8px;width:190px;font-weight:400">Lorem ipsum dolor sit amet, consetetur sadipscing elitr, sed diam nonumy eirmod tempor invidunt ut labore et dolore</p></div>
    <div class="abs footer-col" style="left:386px;top:0"><h5>Sitemap</h5><p>Startseite<br>Anmeldung<br>Aufbauseminar</p></div>
    <div class="abs footer-col" style="left:497px;top:0"><h5>Rechtliches</h5><p>Impressum<br>Datenschutz<br>AGB<br>Cookie-Richtlinien</p></div>
    <div class="abs footer-col" style="left:596px;top:0"><h5>Kontakt</h5><p>Fahrschule Petra Lindqvor<br>Lindenweg 12<br>09111 Musterstadt / OT Talheim</p></div>
  </footer>
</main>

<!-- ============ Mobile view ============ -->
<main class="abs mob">
  <div class="topbar">Schnell, einfach, erfolgreich jetzt<br>Führerschein machen!</div>
  <div class="hero" role="img" aria-label="Foto: schwarzes Auto fährt mit Bewegungsunschärfe im Abendlicht"></div>
  <div class="site-head" style="top:48px;height:42px"></div>
  <div class="abs brand" style="left:13px;top:56px;font-size:10px;line-height:12px"><small style="font-size:8px">Fahrschule</small><b style="font-weight:400">Petra Lindqvor</b></div>
  <svg class="abs" style="left:211px;top:68px" width="16" height="12"><path d="M0 1h16M0 6h16M0 11h16" stroke="#111" stroke-width="1.8"/></svg>
  <div class="abs" style="left:0;top:252px;width:244px;height:14px;background:var(--white)"></div>
  <h1 class="abs" style="left:0;top:257px;width:244px;text-align:center;font-size:18px;line-height:24px;font-weight:700;text-transform:uppercase">Dein Führerschein<br>in <span class="red">Chemnitz</span></h1>
  <p class="abs" style="left:12px;top:306px;width:220px;text-align:center">Wir bringen Sie sicher auf die Straße! Als erfahrene Fahrschule bieten wir Ihnen fach- und sachgerechte Fahrausbildung in allen Zweiradklassen und im PKW-Bereich.</p>
  <span class="abs btn" style="left:8px;top:393px;width:228px;height:28px;line-height:28px;font-size:10px">Jetzt anmelden ➚</span>

  <div class="features">
    <div class="feature" style="top:16px"><svg width="18" height="18"><circle cx="9" cy="9" r="7" fill="none" stroke="#e3261b" stroke-width="1.8"/><path d="M9 5v4.5l2.5 1.5" stroke="#e3261b" fill="none" stroke-width="1.4"/></svg><h4>Flexible Kurszeiten</h4><p>Professionelle Anleitung für deinen sicheren Start.</p></div>
    <div class="feature" style="top:138px"><svg width="18" height="18"><rect x="1" y="6" width="16" height="8" rx="3" fill="#c0392b"/></svg><h4>Moderne Fahrzeuge</h4><p>Lerne mit topaktuellen, sicheren Fahrzeugen.</p></div>
    <div class="feature" style="top:260px"><svg width="18" height="18"><rect x="3" y="3" width="12" height="12" rx="2" fill="#d4a21c"/></svg><h4 style="text-transform:none">Erfahrene Fahrlehrer</h4><p>Professionelle Anleitung für deinen sicheren Start.</p></div>
  </div>
  <div class="abs photo" style="left:0;top:821px;width:244px;height:211px" role="img" aria-label="Foto: junge Fahrschülerin am Autofenster zeigt Daumen hoch"></div>

  <section class="abs" style="left:14px;top:1068px;width:220px">
    <h3 style="font-size:11.5px;font-weight:700;text-transform:uppercase">Hier bist du genau <span class="red">richtig</span>!</h3>
    <svg style="margin-top:18px;display:block" width="18" height="18"><circle cx="9" cy="9" r="9" fill="#e3261b"/><path d="M5 9.3l2.8 2.8 5-5.4" stroke="#fff" stroke-width="1.8" fill="none"/></svg>
    <h4 style="font-size:9.5px;font-weight:700;margin-top:6px;font-family:'Open Sans',sans-serif">Begleitung mit Lern-App</h4>
    <p>Wir begleiten Deinen Lernfortschritt mit einer Lern-App für unterwegs.<br>So bist Du auf Deine Theorieprüfung optimal vorbereitet.</p>
    <svg style="margin-top:18px;display:block" width="18" height="18"><circle cx="9" cy="9" r="9" fill="#e3261b"/><path d="M5 9.3l2.8 2.8 5-5.4" stroke="#fff" stroke-width="1.8" fill="none"/></svg>
    <h4 style="font-size:9.5px;font-weight:700;margin-top:6px;font-family:'Open Sans',sans-serif">Keine lästigen Behördengänge</h4>
    <p>Deine Anmelde- und Prüfungsunterlagen musst Du nicht selbst zu den Ämtern tragen. Wir übernehmen Deine Behördengänge und kümmern uns um eine reibungslose Abwicklung.</p>
    <svg style="margin-top:18px;display:block" width="18" height="18"><circle cx="9" cy="9" r="9" fill="#e3261b"/><path d="M5 9.3l2.8 2.8 5-5.4" stroke="#fff" stroke-width="1.8" fill="none"/></svg>
    <h4 style="font-size:9.5px;font-weight:700;margin-top:6px;font-family:'Open Sans',sans-serif">Einzigartige Lernatmosphäre</h4>
    <p>In lockerer Atmosphäre wirst Du alles lernen, was Du zum Bestehen Deiner theoretischen und praktischen Prüfung brauchst. Erlebe eine herzliche, humorvolle und kompetente Ausbildung und kröne das Ganze mit Deinem Führerschein.</p>
  </section>
  <span class="abs btn" style="left:9px;top:1590px;width:228px;height:28px;line-height:28px;font-size:10px">Jetzt anmelden ➚</span>

  <div class="abs deco" style="left:50px;top:1693px;width:70px;height:80px"></div>
  <h2 class="abs" style="left:9px;top:1730px;width:235px;font-size:11.5px;line-height:19px;font-weight:700;text-transform:uppercase">Folgende <span class="red">Führerscheinklassen</span><br>kannst du bei uns machen.</h2>

  <div class="card m-card" style="top:1796px"><div class="car"></div><h4>BF 17 | PKW ab 17 Jahren</h4><p>Lorem ipsum dolor sit amet, consetetur sadipscing elitr, sed diam nonumy eirmod tempor invidunt ut labore et dolore magna aliquyam erat, sed diam voluptua. At vero eos et accusam et justo duo dolores et ea</p></div>
  <div class="card m-card" style="top:2010px"><div class="car"></div><h4>BF 17 | PKW ab 17 Jahren</h4><p>Lorem ipsum dolor sit amet, consetetur sadipscing elitr, sed diam nonumy eirmod tempor invidunt ut labore et dolore magna aliquyam erat, sed diam voluptua. At vero eos et accusam et justo duo dolores et ea</p></div>
  <div class="card m-card" style="top:2227px"><div class="car" style="background:linear-gradient(180deg,#2f5fc4,#1c3a8a);height:28px"></div><h4>BE | PKW mit Anhänger</h4><p>Lorem ipsum dolor sit amet, consetetur sadipscing elitr, sed diam nonumy eirmod tempor invidunt ut labore et dolore magna aliquyam erat, sed diam voluptua. At vero eos et accusam et justo duo dolores et ea</p></div>
  <span class="abs btn" style="left:72px;top:2447px;width:100px;height:25px;line-height:25px;font-size:9.5px;border-radius:5px">Mehr erfahren</span>
</main>

</body>
</html>
```